aesthetic packaging for down comforter company

Hi guys,

I'm looking for a creative, aesthetic, serious, premium & luxury package design for a down comforter product. The box will be 50cm x 25cm x 25 cm.

please use our logo as reference to show how premium our product is

A small description of what is our product. It is a downcomforter blanket that caters to ALL-SEASONS. Size will be both Queen and King. So please add an option where it can be marked as one of the options.

It is a baffle box design. The product is DESIGNED IN AUSTRALIA, please add this key point

Down is a natural material and the higher the Down content, the lighter and softer the product. Down differs considerably from feathers, as it does not have the hard quill shafts that is common to feather. It is the fluffy filament which comes from the breast of a duck and is an extremely efficient natural insulator.

Target Market(s)

mothers,moms, ladies,girls

Requirements
Nice to have
• feathers, beds ,linen, anything to do with bedding if possible. Try to minimize pictures

```html
<!DOCTYPE html>
<html lang="en">
<head>
<meta charset="utf-8">
<title>Lulldown Down Comforter – Box Dieline</title>
<link rel="stylesheet" href="https://fonts.googleapis.com/css2?family=Roboto+Condensed:wght@400;700&display=swap">
<style>
  :root {
    --paper: #ffffff;
    --cut-line: #3a3a3a;
    --lime: #c3d82e;
    --olive: #968137;
    --gold: #9c7a2c;
    --ring: #f2e600;
    --ink: #1c1c1c;
    --text-light: #ffffff;
    --quilt-light: #ffffff;
    --quilt-shade: #cfcfcf;
  }
  * { margin: 0; padding: 0; box-sizing: border-box; }
  html, body { width: 1200px; height: 423px; overflow: hidden; background: var(--paper); }
  .dieline {
    position: relative;
    width: 1200px;
    height: 423px;
    font-family: "Roboto Condensed", "Arial Narrow", sans-serif;
  }
  .dieline__art { position: absolute; inset: 0; }
  .flap { fill: var(--paper); stroke: var(--cut-line); stroke-width: 0.8; }
  .band { fill: var(--lime); }
  .band-edge { fill: none; stroke: var(--cut-line); stroke-width: 0.8; }
  .wedge { fill: var(--olive); }
  .quilt-window { stroke: var(--ring); stroke-width: 2.5; }

  .brand-name {
    position: absolute;
    color: var(--gold);
    font-weight: 700;
    text-align: center;
    letter-spacing: 0.5px;
  }
  .brand-name--small { font-size: 10px; width: 80px; }
  .brand-name--large { font-size: 15px; width: 110px; }

  .origin-note {
    position: absolute;
    text-align: center;
    color: var(--ink);
    font-weight: 700;
    line-height: 1.2;
  }
  .origin-note--small { width: 90px; font-size: 7px; }
  .origin-note--small .origin-note__key { font-size: 9px; }
  .origin-note--large { width: 120px; font-size: 9.5px; }
  .origin-note--large .origin-note__key { font-size: 11.5px; display: block; margin-top: 2px; }

  .company-lines {
    position: absolute;
    font-size: 8.5px;
    font-weight: 700;
    color: var(--ink);
    line-height: 1.35;
    white-space: nowrap;
  }

  .down-story {
    position: absolute;
    width: 113px;
    font-size: 8.4px;
    font-weight: 700;
    color: var(--text-light);
    line-height: 1.38;
    text-align: justify;
  }
</style>
</head>
<body>
<div class="dieline">
  <svg class="dieline__art" width="1200" height="423" viewBox="0 0 1200 423" xmlns="http://www.w3.org/2000/svg">
    <defs>
      <radialGradient id="quilt-tone" cx="50%" cy="45%" r="60%">
        <stop offset="0%" stop-color="var(--quilt-light)"/>
        <stop offset="100%" stop-color="var(--quilt-shade)"/>
      </radialGradient>
    </defs>

    <!-- glue flap -->
    <polygon class="flap" points="20,114 4,120 4,302 20,308"/>

    <!-- top dust flaps -->
    <polygon class="flap" points="20,114 24,16 214,16 218,114"/>
    <polygon class="flap" points="218,114 222,16 606,16 610,114"/>
    <polygon class="flap" points="610,114 614,16 802,16 806,114"/>
    <polygon class="flap" points="806,114 810,16 1196,16 1200,114"/>

    <!-- bottom dust flaps -->
    <polygon class="flap" points="20,308 24,408 214,408 218,308"/>
    <polygon class="flap" points="218,308 222,408 606,408 610,308"/>
    <polygon class="flap" points="610,308 614,408 802,408 806,308"/>
    <polygon class="flap" points="806,308 810,408 1196,408 1200,308"/>

    <!-- main printed band -->
    <rect class="band" x="20" y="114" width="1180" height="194"/>

    <!-- side panel (narrow) -->
    <g class="panel panel--side">
      <circle class="wedge" cx="160" cy="208" r="68"/>
      <circle class="quilt-window" cx="148" cy="216" r="64" fill="url(#quilt-tone)" role="img" aria-label="Photo of a white baffle-box down comforter"/>
    </g>
    <g class="panel panel--side" transform="translate(590 0)">
      <circle class="wedge" cx="160" cy="208" r="68"/>
      <circle class="quilt-window" cx="148" cy="216" r="64" fill="url(#quilt-tone)" role="img" aria-label="Photo of a white baffle-box down comforter"/>
    </g>

    <!-- front panel (wide) -->
    <g class="panel panel--front">
      <polygon class="wedge" points="372,152 610,114 610,308 395,302"/>
      <circle class="wedge" cx="392" cy="218" r="80"/>
      <circle class="quilt-window" cx="380" cy="226" r="74" fill="url(#quilt-tone)" role="img" aria-label="Photo of a white baffle-box down comforter"/>
    </g>
    <g class="panel panel--front" transform="translate(588 0)">
      <polygon class="wedge" points="372,152 612,114 612,308 395,302"/>
      <circle class="wedge" cx="392" cy="218" r="80"/>
      <circle class="quilt-window" cx="380" cy="226" r="74" fill="url(#quilt-tone)" role="img" aria-label="Photo of a white baffle-box down comforter"/>
    </g>

    <!-- folds and band edges -->
    <rect class="band-edge" x="20" y="114" width="1180" height="194"/>
    <line class="band-edge" x1="218" y1="114" x2="218" y2="308"/>
    <line class="band-edge" x1="610" y1="114" x2="610" y2="308"/>
    <line class="band-edge" x1="806" y1="114" x2="806" y2="308"/>
  </svg>

  <!-- side panel 1 -->
  <div class="brand-name brand-name--small" style="left:12px; top:142px;">LULLDOWN</div>
  <div class="origin-note origin-note--small" style="left:7px; top:246px;">The product<br>is DESIGNED<br><span class="origin-note__key">IN AUSTRALIA</span></div>
  <div class="company-lines" style="left:62px; top:280px;">Company Name......................<br>Address...............................</div>

  <!-- front panel 1 -->
  <div class="brand-name brand-name--large" style="left:211px; top:165px;">LULLDOWN</div>
  <div class="origin-note origin-note--large" style="left:206px; top:265px;">The product<br>is DESIGNED<span class="origin-note__key">IN AUSTRALIA</span></div>
  <p class="down-story" style="left:485px; top:155px;">Down is a natural material and the higher the Down content, the lighter and softer the product. Down differs considerably from feathers, as it does not have the hard quill shafts that is common to feather. It is the fluffy filament which comes from the breast of a duck and is an extremely efficient natural insulator.</p>

  <!-- side panel 2 -->
  <div class="brand-name brand-name--small" style="left:602px; top:142px;">LULLDOWN</div>
  <div class="origin-note origin-note--small" style="left:597px; top:246px;">The product<br>is DESIGNED<br><span class="origin-note__key">IN AUSTRALIA</span></div>
  <div class="company-lines" style="left:652px; top:280px;">Company Name......................<br>Address...............................</div>

  <!-- front panel 2 -->
  <div class="brand-name brand-name--large" style="left:799px; top:165px;">LULLDOWN</div>
  <div class="origin-note origin-note--large" style="left:794px; top:265px;">The product<br>is DESIGNED<span class="origin-note__key">IN AUSTRALIA</span></div>
  <p class="down-story" style="left:1073px; top:155px;">Down is a natural material and the higher the Down content, the lighter and softer the product. Down differs considerably from feathers, as it does not have the hard quill shafts that is common to feather. It is the fluffy filament which comes from the breast of a duck and is an extremely efficient natural insulator.</p>
</div>
</body>
</html>
```